Veterinary company needs powerpoint design

Our veterinary company working with in vitro fertilization needs a professional power point design and business card design.
for the power point desing we would like frontpage, plain slides, table slides, figure slides etc.
the colours should be matching our logo in blue-ish: blue, purple, grey, turquoise
We like it minimalistic, elegant, serious but with a warm touch.

Target Market(s)

Academic,

Industry/Entity Type

Veterinary

Contact Information for Business Card

name, title, email, phone, website

Font styles to use
Sans Serif

Colors
0455a3
3277b5
85abd2
cfdeed
6b449b
886aae
b8a6cd
e4daeb
86cfc6

```html
<!DOCTYPE html>
<html lang="en">
<head>
<meta charset="utf-8">
<title>Norvane presentation template</title>
<link href="https://fonts.googleapis.com/css2?family=Open+Sans:wght@400;600;700&display=swap" rel="stylesheet">
<style>
:root{
  --stage:#cacaca;
  --navy:#134a7e;
  --blue:#0455a3;
  --mid:#3277b5;
  --sky:#85abd2;
  --pale:#cfdeed;
  --grey:#8a8a8a;
  --grey-dk:#6f6f6f;
  --grey-lt:#ececec;
  --text:#7a7a7a;
  --white:#fff;
}
*{box-sizing:border-box;margin:0;padding:0}
html,body{width:1045px;height:1200px;overflow:hidden}
body{background:var(--stage);font-family:"Open Sans",Arial,sans-serif;position:relative}
.slide{position:absolute;width:209px;height:117px;background:var(--white);overflow:hidden}
.slide::after{content:"";position:absolute;left:22px;right:6px;bottom:6px;height:.4px;background:#d6d6d6}
.slide.no-rule::after{display:none}
.abs{position:absolute}
.ttl{position:absolute;left:11px;top:7px;font-weight:700;font-size:3.8px;color:#222;letter-spacing:.1px}
.brand{position:absolute;left:6px;bottom:3px;font-weight:700;font-size:3.2px;color:var(--navy);display:flex;align-items:center;gap:1px}
.brand i{width:2.4px;height:2.4px;border-radius:50%;background:var(--navy);display:block}
.lorem{font-size:2.1px;line-height:2.9px;color:var(--text)}
.lorem.w{color:#e8eef6}
.cap{font-weight:700;font-size:2.4px;color:var(--navy)}
.photo{position:absolute}
.ph-blue{background:linear-gradient(135deg,#2e5f8e,#7ea2c4 55%,#1f4c78)}
.ph-city{background:linear-gradient(160deg,#6f8fb0,#b9c9d9 40%,#3d6590)}
.ph-office{background:linear-gradient(120deg,#8c7e70,#c9c3bb 50%,#6c7a88)}
.ph-warm{background:linear-gradient(120deg,#a28a74,#d8c8b6 50%,#7d8a96)}
.ph-grey{background:linear-gradient(150deg,#9aa3ab,#d9dde1 60%,#8e98a2)}
.box{position:absolute;background:var(--navy);color:#fff;font-weight:700;font-size:2.4px;display:flex;align-items:center;justify-content:center;text-align:center}
.box.g{background:var(--grey)}
.circ{position:absolute;border-radius:50%;background:var(--navy)}
.circ.g{background:var(--grey)}
.ic{position:absolute;left:30%;top:30%;width:40%;height:40%;background:#fff;border-radius:1px}
.ic.r{border-radius:50%}
.line{position:absolute;background:#9a9a9a}
</style>
</head>
<body>

<!-- Row 1 -->
<section class="slide no-rule" style="left:69px;top:58px">
  <div class="photo ph-blue" style="left:0;top:0;width:209px;height:94px;background:linear-gradient(135deg,#1b4f84,#3f73a6 50%,#1a4b7c)" role="img" aria-label="Photo of hands working at a desk, tinted blue"></div>
  <div class="abs" style="left:18px;top:36px;color:#fff;font-weight:700;font-size:7px">Edit title here</div>
  <div class="abs" style="left:18px;top:46px;color:#dfe8f2;font-size:4px">Edit subtitle here</div>
  <div class="brand" style="left:10px;bottom:6px;font-size:4px"><i></i>NORVANE</div>
  <div class="abs" style="right:12px;bottom:10px;font-size:3px;font-weight:700;color:var(--navy)">www.norvanevet.com</div>
</section>

<section class="slide" style="left:296px;top:58px">
  <div class="ttl">ABOUT US</div>
  <div class="abs" style="left:11px;top:26px;width:78px;height:75px;background:var(--navy);padding:8px 6px">
    <p class="lorem w">Lorem ipsum dolor sit amet, consectetur adipiscing elit. Mauris porttitor lacus ut sapien euismod, vitae commodo massa efficitur. Praesent tincidunt consectetur ante, non malesuada lectus elementum. Donec nibh leo, faucibus nec arcu id, condimentum tincidunt nisl. Nam pharetra risus ligula, eu tristique sem dictum vel. Sed vestibulum lectus felis.</p>
  </div>
  <div class="photo ph-blue" style="left:89px;top:26px;width:110px;height:75px;background:linear-gradient(120deg,#a07f6e,#d7c2b4 40%,#4c6f9a 70%,#213f68)" role="img" aria-label="Photo of a team reviewing charts on a table"></div>
  <div class="brand"><i></i>NORVANE</div>
</section>

<section class="slide" style="left:524px;top:58px">
  <div class="ttl">OUR TEAM</div>
  <div class="circ g" style="left:26px;top:32px;width:24px;height:24px;background:#a8a8a8" role="img" aria-label="Portrait of team member"></div>
  <div class="circ g" style="left:70px;top:32px;width:24px;height:24px;background:#9c9c9c" role="img" aria-label="Portrait of team member"></div>
  <div class="circ g" style="left:114px;top:32px;width:24px;height:24px;background:#a2a2a2" role="img" aria-label="Portrait of team member"></div>
  <div class="circ g" style="left:158px;top:32px;width:24px;height:24px;background:#9a9a9a" role="img" aria-label="Portrait of team member"></div>
  <div class="abs" style="left:18px;top:59px;width:40px;text-align:center"><div class="cap">CLARA HOLM</div><div class="lorem">General Manager</div></div>
  <div class="abs" style="left:62px;top:59px;width:40px;text-align:center"><div class="cap">PETER LUND</div><div class="lorem">Trainer Head</div></div>
  <div class="abs" style="left:106px;top:59px;width:40px;text-align:center"><div class="cap">MARK BERG</div><div class="lorem">Finance</div></div>
  <div class="abs" style="left:150px;top:59px;width:40px;text-align:center"><div class="cap">ERIK VANG</div><div class="lorem">Senior Trainer</div></div>
  <p class="lorem abs" style="left:20px;top:72px;width:169px;text-align:center">Lorem ipsum dolor sit amet, consectetur adipiscing elit, sed do eiusmod tempor incididunt ut labore et dolore magna aliqua. Ut enim ad minim veniam, quis nostrud exercitation ullamco laboris nisi ut aliquip ex ea commodo consequat. Duis aute irure dolor in reprehenderit in voluptate velit esse cillum dolore eu fugiat nulla pariatur.</p>
  <div class="brand"><i></i>NORVANE</div>
</section>

<section class="slide" style="left:750px;top:58px">
  <div class="ttl">OUR SERVICES</div>
  <div class="abs" style="left:0;top:18px;width:209px;height:92px;background:var(--grey-lt)"></div>
  <div class="abs" style="left:10px;top:25px;width:190px;display:grid;grid-template-columns:repeat(5,1fr);row-gap:8px;text-align:center">
    <div><div style="width:6px;height:6px;margin:0 auto 2px;background:var(--navy);border-radius:50%"></div><div class="cap">LOREM IPSUM</div><p class="lorem">Lorem ipsum dolor sit amet, consectetur adipiscing elit.</p></div>
    <div><div style="width:6px;height:6px;margin:0 auto 2px;background:var(--navy);border-radius:1px"></div><div class="cap">LOREM IPSUM</div><p class="lorem">Lorem ipsum dolor sit amet, consectetur adipiscing elit.</p></div>
    <div><div style="width:6px;height:6px;margin:0 auto 2px;background:var(--navy)"></div><div class="cap">LOREM IPSUM</div><p class="lorem">Lorem ipsum dolor sit amet, consectetur adipiscing elit.</p></div>
    <div><div style="width:6px;height:6px;margin:0 auto 2px;background:var(--navy);border-radius:50%"></div><div class="cap">LOREM IPSUM</div><p class="lorem">Lorem ipsum dolor sit amet, consectetur adipiscing elit.</p></div>
    <div><div style="width:6px;height:5px;margin:0 auto 3px;background:var(--navy)"></div><div class="cap">LOREM IPSUM</div><p class="lorem">Lorem ipsum dolor sit amet, consectetur adipiscing elit.</p></div>
    <div><div style="width:6px;height:6px;margin:0 auto 2px;border:1.2px solid var(--navy);border-radius:50%"></div><div class="cap">LOREM IPSUM</div><p class="lorem">Lorem ipsum dolor sit amet, consectetur adipiscing elit.</p></div>
    <div><div style="width:6px;height:6px;margin:0 auto 2px;background:var(--navy);border-radius:50%"></div><div class="cap">LOREM IPSUM</div><p class="lorem">Lorem ipsum dolor sit amet, consectetur adipiscing elit.</p></div>
    <div><div style="width:6px;height:5px;margin:0 auto 3px;background:var(--navy);border-radius:1px"></div><div class="cap">LOREM IPSUM</div><p class="lorem">Lorem ipsum dolor sit amet, consectetur adipiscing elit.</p></div>
    <div><div style="width:6px;height:6px;margin:0 auto 2px;border:1.2px solid var(--navy)"></div><div class="cap">LOREM IPSUM</div><p class="lorem">Lorem ipsum dolor sit amet, consectetur adipiscing elit.</p></div>
    <div><div style="width:6px;height:6px;margin:0 auto 2px;background:var(--navy)"></div><div class="cap">LOREM IPSUM</div><p class="lorem">Lorem ipsum dolor sit amet, consectetur adipiscing elit.</p></div>
  </div>
  <div class="brand"><i></i>NORVANE</div>
</section>

<!-- Row 2 -->
<section class="slide" style="left:69px;top:193px">
  <div class="ttl">EDIT TITLE HERE</div>
  <svg class="abs" style="left:0;top:0" width="209" height="117">
    <g stroke="#9a9a9a" stroke-width=".5" fill="none">
      <path d="M52 38H107 M34 42V103 M34 76H58 M34 96H58 M107 38V103 M107 76H132 M107 96H132 M157 38V96 M133 38H157"/>
    </g>
  </svg>
  <div class="box" style="left:14px;top:33px;width:38px;height:10px;font-size:3.4px">TRAINING</div>
  <div class="box" style="left:107px;top:34px;width:38px;height:8px">LEVEL</div>
  <div class="box g" style="left:157px;top:34px;width:38px;height:8px">LEVEL</div>
  <div class="box g" style="left:58px;top:72px;width:38px;height:8px">LEVEL</div>
  <div class="box" style="left:107px;top:72px;width:38px;height:8px">LEVEL</div>
  <div class="box g" style="left:157px;top:72px;width:38px;height:8px">LEVEL</div>
  <div class="box g" style="left:58px;top:96px;width:38px;height:8px">LEVEL</div>
  <div class="box" style="left:107px;top:96px;width:38px;height:8px">LEVEL</div>
  <div class="box g" style="left:157px;top:96px;width:38px;height:8px">LEVEL</div>
  <div class="brand"><i></i>NORVANE</div>
</section>

<section class="slide" style="left:296px;top:193px">
  <div class="ttl">EDIT TITLE HERE</div>
  <svg class="abs" style="left:10px;top:22px" width="100" height="80">
    <g stroke="#ddd" stroke-width=".3"><path d="M12 10H90 M12 20H90 M12 30H90 M12 40H90 M12 50H90 M12 60H90"/></g>
    <path d="M12 5V70H90" stroke="#aaa" stroke-width=".4" fill="none"/>
    <g fill="var(--navy)">
      <rect x="16" y="61" width="7" height="9"/><rect x="30" y="54" width="7" height="16"/>
      <rect x="44" y="48" width="7" height="22"/><rect x="58" y="43" width="7" height="27"/>
      <rect x="72" y="30" width="7" height="40"/>
    </g>
    <path d="M19 58L33 52L47 44L61 38L80 22" stroke="#555" stroke-width=".4" fill="none"/>
    <g fill="var(--navy)"><circle cx="8" cy="78" r="2.2"/><circle cx="26" cy="78" r="2.2"/><circle cx="44" cy="78" r="2.2"/><circle cx="62" cy="78" r="2.2"/><circle cx="80" cy="78" r="2.2"/></g>
  </svg>
  <p class="lorem abs" style="left:118px;top:21px;width:80px">Lorem ipsum dolor sit amet, consectetur adipiscing elit, sed do eiusmod tempor incididunt ut labore et dolore magna aliqua. Ut enim ad minim veniam, quis nostrud exercitation ullamco laboris nisi ut aliquip ex ea commodo consequat. Duis aute irure dolor in reprehenderit in voluptate velit esse cillum dolore eu fugiat nulla pariatur. Excepteur sint occaecat cupidatat non proident, sunt in culpa qui officia deserunt mollit anim id est laborum. Sed ut perspiciatis unde omnis iste natus error sit voluptatem accusantium doloremque laudantium, totam rem aperiam, eaque ipsa quae ab illo inventore veritatis et quasi architecto beatae vitae dicta sunt explicabo. Nemo enim ipsam voluptatem quia voluptas sit aspernatur aut odit aut fugit.</p>
  <div class="brand"><i></i>NORVANE</div>
</section>

<section class="slide" style="left:524px;top:193px">
  <div class="ttl">EDIT TITLE HERE</div>
  <div class="abs" style="left:11px;top:22px;display:grid;grid-template-columns:24px repeat(5,28px);grid-auto-rows:12px;gap:2.5px 3px">
    <div></div><div class="box" style="position:static;height:5px">LOREM IPSUM</div><div class="box" style="position:static;height:5px">LOREM IPSUM</div><div class="box" style="position:static;height:5px">LOREM IPSUM</div><div class="box" style="position:static;height:5px">LOREM IPSUM</div><div class="box" style="position:static;height:5px">LOREM IPSUM</div>
    <div class="box g" style="position:static">LOREM IPSUM</div><div class="box" style="position:static">LOREM IPSUM</div><div class="box" style="position:static">LOREM IPSUM</div><div class="box" style="position:static">LOREM IPSUM</div><div class="box" style="position:static">LOREM IPSUM</div><div class="box" style="position:static">LOREM IPSUM</div>
    <div class="box g" style="position:static">LOREM IPSUM</div><div class="box" style="position:static">LOREM IPSUM</div><div class="box" style="position:static">LOREM IPSUM</div><div class="box" style="position:static">LOREM IPSUM</div><div class="box" style="position:static">LOREM IPSUM</div><div class="box" style="position:static">LOREM IPSUM</div>
    <div class="box g" style="position:static">LOREM IPSUM</div><div class="box" style="position:static">LOREM IPSUM</div><div class="box" style="position:static">LOREM IPSUM</div><div class="box" style="position:static">LOREM IPSUM</div><div class="box" style="position:static">LOREM IPSUM</div><div class="box" style="position:static">LOREM IPSUM</div>
    <div class="box g" style="position:static">LOREM IPSUM</div><div class="box" style="position:static">LOREM IPSUM</div><div class="box" style="position:static">LOREM IPSUM</div><div class="box" style="position:static">LOREM IPSUM</div><div class="box" style="position:static">LOREM IPSUM</div><div class="box" style="position:static">LOREM IPSUM</div>
  </div>
  <div class="brand"><i></i>NORVANE</div>
</section>

<section class="slide" style="left:750px;top:193px">
  <div class="ttl">EDIT TITLE HERE</div>
  <div class="photo" style="left:11px;top:20px;width:60px;height:48px;background:linear-gradient(135deg,#3d6b8c,#b6ad8e 55%,#5a6c5c)" role="img" aria-label="Photo of laptop on a desk"></div>
  <div class="photo" style="left:75px;top:20px;width:60px;height:48px;background:linear-gradient(135deg,#cfd8e2,#7ea8cf 50%,#e8eef3)" role="img" aria-label="Photo of hand holding a tablet with charts"></div>
  <div class="photo" style="left:139px;top:20px;width:60px;height:48px;background:linear-gradient(160deg,#4b7aa7,#9fb8d0 45%,#2a5280)" role="img" aria-label="Photo of city towers with data overlay"></div>
  <div class="abs" style="left:11px;top:71px;width:60px;text-align:center"><div class="cap">LOREM IPSUM</div><p class="lorem">Lorem ipsum dolor sit amet, consectetur adipiscing elit. Curabitur odio ligula, ultrices eu consectetur.</p></div>
  <div class="abs" style="left:75px;top:71px;width:60px;text-align:center"><div class="cap">LOREM IPSUM</div><p class="lorem">Lorem ipsum dolor sit amet, consectetur adipiscing elit. Curabitur odio ligula, ultrices eu consectetur.</p></div>
  <div class="abs" style="left:139px;top:71px;width:60px;text-align:center"><div class="cap">LOREM IPSUM</div><p class="lorem">Lorem ipsum dolor sit amet, consectetur adipiscing elit. Curabitur odio ligula, ultrices eu consectetur.</p></div>
  <div class="brand"><i></i>NORVANE</div>
</section>

<!-- Row 3 -->
<section class="slide no-rule" style="left:69px;top:327px">
  <div class="photo ph-city" style="left:0;top:0;width:209px;height:117px;background:linear-gradient(110deg,#3b6690,#8fa9c4 45%,#2c5784 75%,#6d8db0)" role="img" aria-label="Photo of coin stacks and city skyline, tinted blue"></div>
  <div class="abs" style="left:12px;top:0;width:84px;height:117px;background:rgba(19,74,126,.82);padding:32px 10px 0;text-align:center">
    <div style="color:#fff;font-weight:700;font-size:6px;margin-bottom:3px">Section Title</div>
    <p class="lorem w" style="font-size:2.5px;line-height:3.3px">Lorem ipsum dolor sit amet, consectetur adipiscing elit. Curabitur odio ligula, ultrices eu consectetur, condimentum at magna. Sed finibus, felis ullamcorper interdum ullamcorper, libero ex.</p>
  </div>
</section>

<section class="slide" style="left:296px;top:327px">
  <div class="ttl">EDIT TITLE HERE</div>
  <div class="photo" style="left:0;top:19px;width:209px;height:88px;background:linear-gradient(120deg,#1f4c78,#5c84ad 40%,#a7b5c2 70%,#6e7f90)" role="img" aria-label="Photo of a laboratory bench, tinted blue"></div>
  <div class="abs" style="left:0;top:19px;width:58px;height:88px;background:rgba(19,74,126,.9);padding:18px 5px 0;text-align:center"><p class="lorem w" style="font-size:2.5px;line-height:3.3px;font-weight:700">Lorem ipsum dolor sit amet consectetur adipiscing elit. Cras bibendum mattis leo, ac efficitur ipsum lobortis non. Praesent vitae pulvinar lorem ipsum dolor sit amet.</p></div>
  <div class="abs" style="left:59px;top:40px;width:138px;height:40px;background:#fff;display:flex;justify-content:space-around;align-items:center;padding-top:4px">
    <div style="text-align:center"><div style="width:6px;height:6px;margin:0 auto 2px;background:var(--navy)"></div><div class="cap">LOREM</div></div>
    <div style="text-align:center"><div style="width:6px;height:6px;margin:0 auto 2px;background:var(--navy);clip-path:polygon(50% 0,100% 45%,85% 45%,85% 100%,15% 100%,15% 45%,0 45%)"></div><div class="cap">LOREM</div></div>
    <div style="text-align:center"><div style="width:6px;height:6px;margin:0 auto 2px;border:1.5px solid var(--navy);border-radius:50%"></div><div class="cap">LOREM</div></div>
  </div>
  <div class="brand"><i></i>NORVANE</div>
</section>

<section class="slide" style="left:524px;top:327px">
  <div class="ttl">EDIT TITLE HERE</div>
  <div class="abs" style="left:28px;top:20px;display:grid;grid-template-columns:repeat(3,48px);grid-auto-rows:38px;gap:6px 6px">
    <div style="border:.5px solid #b9c6d4;text-align:center;padding:8px 3px 0;position:relative"><div style="position:absolute;left:19px;top:-1px;width:10px;height:9px;background:var(--navy);clip-path:polygon(0 0,100% 0,100% 70%,50% 100%,0 70%)"></div><div class="cap" style="margin-top:2px">LOREM IPSUM</div><p class="lorem">Lorem ipsum dolor sit amet, lorem ipsum dolor sit amet consectetur.</p></div>
    <div style="border:.5px solid #b9c6d4;text-align:center;padding:8px 3px 0;position:relative"><div style="position:absolute;left:19px;top:-1px;width:10px;height:9px;background:var(--navy);clip-path:polygon(0 0,100% 0,100% 70%,50% 100%,0 70%)"></div><div class="cap" style="margin-top:2px">LOREM IPSUM</div><p class="lorem">Lorem ipsum dolor sit amet, lorem ipsum dolor sit amet consectetur.</p></div>
    <div style="border:.5px solid #b9c6d4;text-align:center;padding:8px 3px 0;position:relative"><div style="position:absolute;left:19px;top:-1px;width:10px;height:9px;background:var(--navy);clip-path:polygon(0 0,100% 0,100% 70%,50% 100%,0 70%)"></div><div class="cap" style="margin-top:2px">LOREM IPSUM</div><p class="lorem">Lorem ipsum dolor sit amet, lorem ipsum dolor sit amet consectetur.</p></div>
    <div style="border:.5px solid #b9c6d4;text-align:center;padding:8px 3px 0;position:relative"><div style="position:absolute;left:19px;top:-1px;width:10px;height:9px;background:var(--navy);clip-path:polygon(0 0,100% 0,100% 70%,50% 100%,0 70%)"></div><div class="cap" style="margin-top:2px">LOREM IPSUM</div><p class="lorem">Lorem ipsum dolor sit amet, lorem ipsum dolor sit amet consectetur.</p></div>
    <div style="border:.5px solid #b9c6d4;text-align:center;padding:8px 3px 0;position:relative"><div style="position:absolute;left:19px;top:-1px;width:10px;height:9px;background:var(--navy);clip-path:polygon(0 0,100% 0,100% 70%,50% 100%,0 70%)"></div><div class="cap" style="margin-top:2px">LOREM IPSUM</div><p class="lorem">Lorem ipsum dolor sit amet, lorem ipsum dolor sit amet consectetur.</p></div>
    <div style="border:.5px solid #b9c6d4;text-align:center;padding:8px 3px 0;position:relative"><div style="position:absolute;left:19px;top:-1px;width:10px;height:9px;background:var(--navy);clip-path:polygon(0 0,100% 0,100% 70%,50% 100%,0 70%)"></div><div class="cap" style="margin-top:2px">LOREM IPSUM</div><p class="lorem">Lorem ipsum dolor sit amet, lorem ipsum dolor sit amet consectetur.</p></div>
  </div>
  <div class="brand"><i></i>NORVANE</div>
</section>

<section class="slide" style="left:750px;top:327px">
  <div class="ttl">EDIT TITLE HERE</div>
  <div class="circ" style="left:18px;top:26px;width:10px;height:10px"><span class="ic"></span></div>
  <div class="circ" style="left:18px;top:48px;width:10px;height:10px"><span class="ic r"></span></div>
  <div class="circ" style="left:18px;top:70px;width:10px;height:10px"><span class="ic"></span></div>
  <div class="circ" style="left:18px;top:92px;width:10px;height:10px"><span class="ic"></span></div>
  <div class="abs" style="left:32px;top:26px;width:60px"><div class="cap">Lorem ipsum dolor</div><p class="lorem">Lorem ipsum dolor sit amet, consectetur adipiscing elit, sed do eiusmod.</p></div>
  <div class="abs" style="left:32px;top:48px;width:60px"><div class="cap">Lorem ipsum dolor</div><p class="lorem">Lorem ipsum dolor sit amet, consectetur adipiscing elit, sed do eiusmod.</p></div>
  <div class="abs" style="left:32px;top:70px;width:60px"><div class="cap">Lorem ipsum dolor</div><p class="lorem">Lorem ipsum dolor sit amet, consectetur adipiscing elit, sed do eiusmod.</p></div>
  <div class="abs" style="left:32px;top:92px;width:60px"><div class="cap">Lorem ipsum dolor</div><p class="lorem">Lorem ipsum dolor sit amet, consectetur adipiscing elit, sed do eiusmod.</p></div>
  <div class="photo" style="left:100px;top:0;width:95px;height:117px;background:linear-gradient(140deg,#d8dfe6,#9eb5cb 40%,#5c7d9e 75%,#c9d2da)" role="img" aria-label="Photo of hands pointing at a tablet with graphs"></div>
  <div class="brand"><i></i>NORVANE</div>
</section>

<!-- Row 4 -->
<section class="slide" style="left:69px;top:462px">
  <div class="ttl">EDIT TITLE HERE</div>
  <p class="lorem abs" style="left:34px;top:24px;width:150px;text-align:center">Lorem ipsum dolor sit amet, consectetur adipiscing elit, sed do eiusmod tempor incididunt ut labore et dolore magna aliqua. Ut enim ad minim veniam, quis nostrud exercitation ullamco laboris nisi ut aliquip ex ea commodo.</p>
  <div class="abs" style="left:0;top:38px;width:209px;height:60px;background:var(--navy)"></div>
  <div class="abs" style="left:10px;top:30px;width:38px;height:52px;background:linear-gradient(160deg,#dfe3e7,#8a939c)" role="img" aria-label="Illustration of a desktop computer monitor"></div>
  <div class="abs" style="left:66px;top:58px;width:130px;display:flex;justify-content:space-between;text-align:center">
    <div style="width:28px"><div style="width:9px;height:9px;margin:0 auto 2px;border:.6px solid #fff;border-radius:50%"></div><p class="lorem w" style="font-weight:700">Lorem ipsum dolor sit amet, consectetur adipiscing elit</p></div>
    <div style="width:28px"><div style="width:9px;height:9px;margin:0 auto 2px;border:.6px solid #fff;border-radius:50%"></div><p class="lorem w" style="font-weight:700">Lorem ipsum dolor sit amet, consectetur adipiscing elit</p></div>
    <div style="width:28px"><div style="width:9px;height:9px;margin:0 auto 2px;border:.6px solid #fff;border-radius:50%"></div><p class="lorem w" style="font-weight:700">Lorem ipsum dolor sit amet, consectetur adipiscing elit</p></div>
    <div style="width:28px"><div style="width:9px;height:9px;margin:0 auto 2px;border:.6px solid #fff;border-radius:50%"></div><p class="lorem w" style="font-weight:700">Lorem ipsum dolor sit amet, consectetur adipiscing elit</p></div>
  </div>
  <div class="brand"><i></i>NORVANE</div>
</section>

<section class="slide" style="left:296px;top:462px">
  <div class="ttl">EDIT TITLE HERE</div>
  <svg class="abs" style="left:0;top:0" width="209" height="117">
    <g stroke="#9a9a9a" stroke-width=".4" fill="none">
      <path d="M102 28V34 M47 34H160 M47 34V39 M160 34V39 M47 43V82H160V43 M102 34V73 M80 43V73H126V43"/>
    </g>
  </svg>
  <div class="box" style="left:85px;top:23px;width:34px;height:5px">Title Goes Here</div>
  <div class="box g" style="left:33px;top:39px;width:28px;height:5px">Title Goes Here</div>
  <div class="box" style="left:68px;top:39px;width:28px;height:5px">Title Goes Here</div>
  <div class="box" style="left:109px;top:39px;width:28px;height:5px">Title Goes Here</div>
  <div class="box g" style="left:146px;top:39px;width:28px;height:5px">Title Goes Here</div>
  <div class="box" style="left:68px;top:52px;width:28px;height:5px">Title Goes Here</div>
  <div class="box" style="left:109px;top:52px;width:28px;height:5px">Title Goes Here</div>
  <div class="box" style="left:68px;top:69px;width:28px;height:5px">Title Goes Here</div>
  <div class="box" style="left:109px;top:69px;width:28px;height:5px">Title Goes Here</div>
  <div class="abs" style="left:0;top:85px;width:209px;height:32px;background:var(--grey-lt);padding:4px 14px"><p class="lorem" style="text-align:center">Lorem ipsum dolor sit amet, consectetur adipiscing elit, sed do eiusmod tempor incididunt ut labore et dolore magna aliqua. Ut enim ad minim veniam, quis nostrud exercitation ullamco laboris nisi ut aliquip ex ea commodo consequat. Duis aute irure dolor in reprehenderit in voluptate velit esse cillum dolore eu fugiat nulla pariatur. Excepteur sint occaecat cupidatat non proident.</p></div>
</section>

<section class="slide" style="left:524px;top:462px">
  <div class="ttl">EDIT TITLE HERE</div>
  <div class="abs" style="left:0;top:18px;width:209px;height:92px;background:var(--grey-lt)"></div>
  <div class="abs" style="left:18px;top:26px;display:grid;grid-template-columns:repeat(3,52px);grid-auto-rows:36px;gap:5px 10px">
    <div style="background:#fff;position:relative"><div class="circ" style="left:19px;top:7px;width:13px;height:13px"><span class="ic r"></span></div><div class="box" style="left:3px;bottom:3px;width:46px;height:4px">LOREM IPSUM DOLOR</div></div>
    <div style="background:#fff;position:relative"><div class="circ" style="left:19px;top:7px;width:13px;height:13px"><span class="ic r"></span></div><div class="box" style="left:3px;bottom:3px;width:46px;height:4px">LOREM IPSUM DOLOR</div></div>
    <div style="background:#fff;position:relative"><div class="circ" style="left:19px;top:7px;width:13px;height:13px"><span class="ic r"></span></div><div class="box" style="left:3px;bottom:3px;width:46px;height:4px">LOREM IPSUM DOLOR</div></div>
    <div style="background:#fff;position:relative"><div class="abs" style="left:20px;top:9px;width:12px;height:9px;background:var(--navy);border-radius:1px"></div><div class="box" style="left:3px;bottom:3px;width:46px;height:4px">LOREM IPSUM DOLOR</div></div>
    <div style="background:#fff;position:relative"><div class="abs" style="left:20px;top:8px;width:12px;height:11px;background:var(--navy)"></div><div class="box" style="left:3px;bottom:3px;width:46px;height:4px">LOREM IPSUM DOLOR</div></div>
    <div style="background:#fff;position:relative"><div class="abs" style="left:21px;top:8px;width:10px;height:12px;border:1.2px solid var(--navy)"></div><div class="box" style="left:3px;bottom:3px;width:46px;height:4px">LOREM IPSUM DOLOR</div></div>
  </div>
  <div class="brand"><i></i>NORVANE</div>
</section>

<section class="slide" style="left:750px;top:462px">
  <div class="ttl">EDIT TITLE HERE</div>
  <table class="abs" style="left:14px;top:34px;width:181px;border-collapse:collapse;font-size:2.6px;color:#555;text-align:center">
    <tr style="background:var(--navy);color:#fff;font-weight:700;height:6px"><td>Lorem</td><td>Lorem</td><td>Lorem</td><td>Lorem</td></tr>
    <tr style="background:#e6e6e6;height:7px"><td>Lorem</td><td>Lorem</td><td>Lorem</td><td>Lorem</td></tr>
    <tr style="height:7px"><td>Lorem</td><td>Lorem</td><td>Lorem</td><td>Lorem</td></tr>
    <tr style="background:#e6e6e6;height:7px"><td>Lorem</td><td>Lorem</td><td>Lorem</td><td>Lorem</td></tr>
    <tr style="height:7px"><td>Lorem</td><td>Lorem</td><td>Lorem</td><td>Lorem</td></tr>
    <tr style="background:#e6e6e6;height:7px"><td>Lorem</td><td>Lorem</td><td>Lorem</td><td>Lorem</td></tr>
    <tr style="height:7px"><td>Lorem</td><td>Lorem</td><td>Lorem</td><td>Lorem</td></tr>
  </table>
  <div class="brand"><i></i>NORVANE</div>
</section>

<!-- Row 5 -->
<section class="slide" style="left:69px;top:597px">
  <div class="ttl">EDIT TITLE HERE</div>
  <p class="lorem abs" style="left:11px;top:24px;width:108px;text-align:center">Lorem ipsum dolor sit amet, consectetur adipiscing elit, sed do eiusmod tempor incididunt ut labore et dolore magna aliqua. Ut enim ad minim veniam, quis nostrud exercitation ullamco laboris nisi ut aliquip ex ea commodo consequat. Duis aute irure dolor in reprehenderit in voluptate velit esse cillum dolore eu fugiat nulla pariatur. Excepteur sint occaecat cupidatat non proident, sunt in culpa qui officia deserunt mollit anim id est laborum.</p>
  <div class="abs" style="left:14px;top:70px;width:104px;display:flex;justify-content:space-between;text-align:center">
    <div style="width:30px"><div style="width:8px;height:8px;margin:0 auto 2px;border:1.2px solid var(--navy)"></div><p class="lorem">Lorem ipsum dolor sit amet, consectetur adipiscing.</p></div>
    <div style="width:30px"><div style="width:8px;height:8px;margin:0 auto 2px;background:linear-gradient(90deg,var(--navy) 20%,transparent 20% 40%,var(--navy) 40% 60%,transparent 60% 80%,var(--navy) 80%)"></div><p class="lorem">Lorem ipsum dolor sit amet, consectetur adipiscing.</p></div>
    <div style="width:30px"><div style="width:8px;height:8px;margin:0 auto 2px;background:var(--navy)"></div><p class="lorem">Lorem ipsum dolor sit amet, consectetur adipiscing.</p></div>
  </div>
  <div class="photo ph-office" style="left:130px;top:0;width:79px;height:117px" role="img" aria-label="Photo of colleagues in a meeting"></div>
  <div class="brand"><i></i>NORVANE</div>
</section>

<section class="slide" style="left:296px;top:597px">
  <div class="ttl">EDIT TITLE HERE</div>
  <div class="abs" style="left:30px;top:26px;width:150px;display:grid;grid-template-columns:1fr 1fr;row-gap:8px;column-gap:10px">
    <div style="display:flex;gap:3px;justify-content:flex-end"><div style="text-align:right"><div class="cap">Lorem ipsum dolor</div><p class="lorem">Lorem ipsum dolor sit amet, consectetur elit.</p></div><div style="flex:0 0 10px;height:10px;border-radius:50%;background:var(--navy)"></div></div>
    <div style="display:flex;gap:3px"><div style="flex:0 0 10px;height:10px;border-radius:50%;background:var(--grey)"></div><div><div class="cap">Lorem ipsum dolor</div><p class="lorem">Lorem ipsum dolor sit amet, consectetur elit.</p></div></div>
    <div style="display:flex;gap:3px;justify-content:flex-end"><div style="text-align:right"><div class="cap">Lorem ipsum dolor</div><p class="lorem">Lorem ipsum dolor sit amet, consectetur elit.</p></div><div style="flex:0 0 10px;height:10px;border-radius:50%;background:var(--navy)"></div></div>
    <div style="display:flex;gap:3px"><div style="flex:0 0 10px;height:10px;border-radius:50%;background:var(--grey)"></div><div><div class="cap">Lorem ipsum dolor</div><p class="lorem">Lorem ipsum dolor sit amet, consectetur elit.</p></div></div>
    <div style="display:flex;gap:3px;justify-content:flex-end"><div style="text-align:right"><div class="cap">Lorem ipsum dolor</div><p class="lorem">Lorem ipsum dolor sit amet, consectetur elit.</p></div><div style="flex:0 0 10px;height:10px;border-radius:50%;background:var(--navy)"></div></div>
    <div style="display:flex;gap:3px"><div style="flex:0 0 10px;height:10px;border-radius:50%;background:var(--grey)"></div><div><div class="cap">Lorem ipsum dolor</div><p class="lorem">Lorem ipsum dolor sit amet, consectetur elit.</p></div></div>
    <div style="display:flex;gap:3px;justify-content:flex-end"><div style="text-align:right"><div class="cap">Lorem ipsum dolor</div><p class="lorem">Lorem ipsum dolor sit amet, consectetur elit.</p></div><div style="flex:0 0 10px;height:10px;border-radius:50%;background:var(--navy)"></div></div>
    <div style="display:flex;gap:3px"><div style="flex:0 0 10px;height:10px;border-radius:50%;background:var(--grey)"></div><div><div class="cap">Lorem ipsum dolor</div><p class="lorem">Lorem ipsum dolor sit amet, consectetur elit.</p></div></div>
  </div>
  <div class="brand"><i></i>NORVANE</div>
</section>

<section class="slide" style="left:524px;top:597px">
  <div class="ttl">EDIT TITLE HERE</div>
  <p class="lorem abs" style="left:11px;top:28px;width:54px">Lorem ipsum dolor sit amet, consectetur adipiscing elit. Donec fermentum, laoreet et eu, sollicitudin mauris felis. Curabitur at purus a sapien facilisis. Sed dictum, turpis ac vulputate. Praesent nibh nisl, faucibus at enim et, ultrices vehicula velit. Aliquam ac sapien ligula. Sed a felis ut diam maximus aliquet.</p>
  <div class="photo" style="left:66px;top:19px;width:143px;height:88px;background:linear-gradient(135deg,#c7ccd1,#77808a 50%,#3f4852)" role="img" aria-label="Photo of hands typing on a keyboard"></div>
  <div class="abs" style="left:68px;top:28px;width:46px;height:72px;background:var(--navy);padding:3px"><div style="color:#fff;font-weight:700;font-size:2.8px;text-align:center;margin-bottom:2px">Lorem ipsum</div><p class="lorem w">Lorem ipsum dolor sit amet, consectetur adipiscing elit. Donec fermentum, laoreet et eu, sollicitudin mauris. Curabitur at purus a sapien facilisis. Sed dictum turpis ac vulputate. Praesent nibh nisl faucibus at enim.</p></div>
  <div class="abs" style="left:117px;top:28px;width:46px;height:72px;background:var(--navy);padding:3px"><div style="color:#fff;font-weight:700;font-size:2.8px;text-align:center;margin-bottom:2px">Lorem ipsum</div><p class="lorem w">Lorem ipsum dolor sit amet, consectetur adipiscing elit. Donec fermentum, laoreet et eu, sollicitudin mauris. Curabitur at purus a sapien facilisis. Sed dictum turpis ac vulputate. Praesent nibh nisl faucibus at enim.</p></div>
  <div class="brand"><i></i>NORVANE</div>
</section>

<section class="slide" style="left:750px;top:597px">
  <div class="ttl">EDIT TITLE HERE</div>
  <div class="photo" style="left:8px;top:24px;width:72px;height:64px;background:linear-gradient(135deg,#8b8f94,#cfd4d9 45%,#6a7886)" role="img" aria-label="Photo of hand holding a smartphone"></div>
  <p class="lorem abs" style="left:96px;top:28px;width:100px;text-align:center">Lorem ipsum dolor sit amet, consectetur adipiscing elit, sed do eiusmod tempor incididunt ut labore et dolore magna aliqua. Ut enim ad minim veniam, quis nostrud exercitation ullamco laboris nisi ut aliquip ex ea commodo consequat. Duis aute irure dolor in reprehenderit in voluptate velit esse cillum dolore.</p>
  <div class="abs" style="left:98px;top:70px;width:100px;display:flex;justify-content:space-between;text-align:center">
    <div style="width:28px"><div style="width:8px;height:8px;margin:0 auto 2px;border:1.2px solid var(--navy)"></div><p class="lorem">Lorem ipsum dolor sit amet, consectetur.</p></div>
    <div style="width:28px"><div style="width:8px;height:8px;margin:0 auto 2px;background:linear-gradient(90deg,var(--navy) 20%,transparent 20% 40%,var(--navy) 40% 60%,transparent 60% 80%,var(--navy) 80%)"></div><p class="lorem">Lorem ipsum dolor sit amet, consectetur.</p></div>
    <div style="width:28px"><div style="width:8px;height:8px;margin:0 auto 2px;background:var(--navy)"></div><p class="lorem">Lorem ipsum dolor sit amet, consectetur.</p></div>
  </div>
  <div class="brand"><i></i>NORVANE</div>
</section>

<!-- Row 6 -->
<section class="slide" style="left:69px;top:734px">
  <div class="ttl">EDIT TITLE HERE</div>
  <div class="photo ph-warm" style="left:0;top:23px;width:104px;height:84px" role="img" aria-label="Photo of a team working together at laptops"></div>
  <div class="abs" style="left:104px;top:23px;width:105px;height:84px;background:var(--navy);padding:6px 6px 0 8px">
    <div style="display:flex;gap:4px;margin-bottom:7px"><div style="flex:0 0 9px;height:7px;background:#fff;border-radius:3px"></div><div><div style="color:#fff;font-weight:700;font-size:2.4px">LOREM IPSUM</div><p class="lorem w">Lorem ipsum dolor sit amet, consectetur adipiscing elit. Curabitur odio ligula, ultrices eu.</p></div></div>
    <div style="display:flex;gap:4px;margin-bottom:7px"><div style="flex:0 0 9px;height:9px;border:1px solid #fff;border-radius:50%"></div><div><div style="color:#fff;font-weight:700;font-size:2.4px">LOREM IPSUM</div><p class="lorem w">Lorem ipsum dolor sit amet, consectetur adipiscing elit. Curabitur odio ligula, ultrices eu.</p></div></div>
    <div style="display:flex;gap:4px"><div style="flex:0 0 9px;height:8px;background:#fff;clip-path:polygon(50% 0,100% 35%,100% 100%,0 100%,0 35%)"></div><div><div style="color:#fff;font-weight:700;font-size:2.4px">LOREM IPSUM</div><p class="lorem w">Lorem ipsum dolor sit amet, consectetur adipiscing elit. Curabitur odio ligula, ultrices eu.</p></div></div>
  </div>
  <div class="brand"><i></i>NORVANE</div>
</section>

<section class="slide" style="left:296px;top:734px">
  <div class="ttl">EDIT TITLE HERE</div>
  <p class="lorem abs" style="left:11px;top:22px;width:90px">Lorem ipsum dolor sit amet, consectetur adipiscing elit, sed do eiusmod tempor incididunt ut labore et dolore magna aliqua. Ut enim ad minim veniam, quis nostrud exercitation ullamco laboris nisi ut aliquip ex ea commodo consequat. Duis aute irure dolor in reprehenderit in voluptate velit esse cillum dolore eu fugiat nulla pariatur. Excepteur sint occaecat cupidatat non proident, sunt in culpa qui officia deserunt mollit anim id est laborum. Sed ut perspiciatis unde omnis iste natus error sit voluptatem accusantium doloremque laudantium, totam rem aperiam eaque ipsa quae ab illo inventore veritatis et quasi architecto beatae vitae dicta sunt explicabo. Nemo enim ipsam voluptatem quia voluptas sit aspernatur aut odit aut fugit, sed quia consequuntur magni dolores eos qui ratione.</p>
  <div class="abs" style="left:100px;top:28px;display:grid;grid-template-columns:repeat(4,17px);grid-auto-rows:16px;gap:1px">
    <div style="background:#8a8a8a"></div><div style="background:var(--navy)"></div><div style="background:#fff"></div><div style="background:#8a8a8a"></div>
    <div style="background:var(--navy)"></div><div style="background:#8a8a8a"></div><div style="background:var(--navy)"></div><div style="background:#fff"></div>
    <div style="background:#8a8a8a"></div><div style="background:var(--navy)"></div><div style="background:#8a8a8a"></div><div style="background:var(--navy)"></div>
  </div>
  <div class="abs" style="left:120px;top:32px;font-size:2.4px;color:#fff;font-weight:700">Lorem</div>
  <div class="abs" style="left:120px;top:48px;font-size:2.4px;color:#fff;font-weight:700">Lorem</div>
  <div class="abs" style="left:152px;top:64px;font-size:2.4px;color:#fff;font-weight:700">Lorem</div>
  <div class="abs" style="left:104px;top:64px;font-size:2.4px;color:#fff;font-weight:700">Lorem</div>
  <div class="abs" style="left:104px;top:92px;display:flex;gap:10px;font-size:2px;color:#888">
    <span>● Lorem</span><span>● Lorem</span><span>● Lorem</span><span>● Lorem</span>
  </div>
  <div class="brand"><i></i>NORVANE</div>
</section>

<section class="slide" style="left:524px;top:734px">
  <div class="ttl">EDIT TITLE HERE</div>
  <svg class="abs" style="left:8px;top:26px" width="140" height="80">
    <path d="M4 58L30 40L58 48L90 22L128 38V66H4Z" fill="var(--sky)"/>
    <path d="M4 62L30 50L58 56L90 38L128 48V66H4Z" fill="var(--mid)"/>
    <path d="M4 66L30 58L58 60L90 52L128 58V66H4Z" fill="var(--navy)"/>
    <path d="M4 66H128" stroke="#999" stroke-width=".4"/>
    <g fill="#8a6d3b"><rect x="22" y="14" width="16" height="4"/><rect x="82" y="12" width="16" height="4"/><rect x="102" y="28" width="16" height="4"/><rect x="10" y="42" width="16" height="4"/><rect x="48" y="40" width="16" height="4"/></g>
    <g fill="#8a6d3b"><circle cx="20" cy="76" r="1.5"/><circle cx="44" cy="76" r="1.5"/><circle cx="68" cy="76" r="1.5"/><circle cx="92" cy="76" r="1.5"/></g>
  </svg>
  <div class="abs" style="left:150px;top:26px;width:50px;height:78px;background:var(--grey-lt);padding:3px"><p class="lorem">Lorem ipsum dolor sit amet, consectetur adipiscing elit, sed do eiusmod tempor incididunt ut labore et dolore magna aliqua. Ut enim ad minim veniam, quis nostrud exercitation ullamco laboris nisi ut aliquip ex ea commodo consequat. Duis aute irure dolor in reprehenderit in voluptate velit esse cillum dolore eu fugiat nulla pariatur. Excepteur sint occaecat cupidatat non proident.</p></div>
  <div class="brand"><i></i>NORVANE</div>
</section>

<section class="slide" style="left:750px;top:734px">
  <div class="ttl">EDIT TITLE HERE</div>
  <div class="abs" style="left:0;top:20px;width:209px;height:90px;background:var(--grey-lt)"></div>
  <div class="abs" style="left:14px;top:32px;width:181px;display:flex;justify-content:space-between;text-align:center">
    <div style="width:38px"><div style="width:17px;height:17px;margin:0 auto 4px;border-radius:50%;background:var(--navy);position:relative"><span class="ic"></span></div><div class="cap" style="color:var(--navy)">Lorem ipsum dolor</div><p class="lorem">Lorem ipsum dolor sit amet, consectetur adipiscing elit. Mauris porttitor lectus ac sapien.</p></div>
    <div style="width:38px"><div style="width:17px;height:17px;margin:0 auto 4px;border-radius:50%;background:var(--navy);position:relative"><span class="ic"></span></div><div class="cap" style="color:var(--navy)">Lorem ipsum dolor</div><p class="lorem">Lorem ipsum dolor sit amet, consectetur adipiscing elit. Mauris porttitor lectus ac sapien.</p></div>
    <div style="width:38px"><div style="width:17px;height:17px;margin:0 auto 4px;border-radius:50%;background:var(--navy);position:relative"><span class="ic"></span></div><div class="cap" style="color:var(--navy)">Lorem ipsum dolor</div><p class="lorem">Lorem ipsum dolor sit amet, consectetur adipiscing elit. Mauris porttitor lectus ac sapien.</p></div>
    <div style="width:38px"><div style="width:17px;height:17px;margin:0 auto 4px;border-radius:50%;background:var(--navy);position:relative"><span class="ic r"></span></div><div class="cap" style="color:var(--navy)">Lorem ipsum dolor</div><p class="lorem">Lorem ipsum dolor sit amet, consectetur adipiscing elit. Mauris porttitor lectus ac sapien.</p></div>
  </div>
  <div class="brand"><i></i>NORVANE</div>
</section>

<!-- Row 7 -->
<section class="slide" style="left:69px;top:869px">
  <div class="ttl">EDIT TITLE HERE</div>
  <p class="lorem abs" style="left:11px;top:18px;width:180px">Lorem ipsum dolor sit amet, consectetur adipiscing elit. Aenean sed tempor lorem. Suspendisse.</p>
  <div class="photo ph-warm" style="left:13px;top:27px;width:183px;height:40px;background:linear-gradient(90deg,#7a8a5c,#c7a58a 30%,#a0715a 60%,#8d8a86)" role="img" aria-label="Photo of four smiling colleagues"></div>
  <div class="abs" style="left:13px;top:72px;width:183px;display:flex;gap:3px">
    <div style="flex:1"><div class="box g" style="position:static;height:6px;font-size:3px">A</div><p class="lorem" style="text-align:center;margin-top:2px">Lorem ipsum dolor sit amet, consectetur adipiscing elit. Suspendisse.</p></div>
    <div style="flex:1"><div class="box" style="position:static;height:6px;font-size:3px">B</div><p class="lorem" style="text-align:center;margin-top:2px">Lorem ipsum dolor sit amet, consectetur adipiscing elit. Suspendisse.</p></div>
    <div style="flex:1"><div class="box g" style="position:static;height:6px;font-size:3px">C</div><p class="lorem" style="text-align:center;margin-top:2px">Lorem ipsum dolor sit amet, consectetur adipiscing elit. Suspendisse.</p></div>
    <div style="flex:1"><div class="box" style="position:static;height:6px;font-size:3px">D</div><p class="lorem" style="text-align:center;margin-top:2px">Lorem ipsum dolor sit amet, consectetur adipiscing elit. Suspendisse.</p></div>
  </div>
  <div class="brand"><i></i>NORVANE</div>
</section>

<section class="slide" style="left:296px;top:869px">
  <div class="ttl">EDIT TITLE HERE</div>
  <div class="photo" style="left:0;top:22px;width:209px;height:86px;background:linear-gradient(120deg,#5a6570,#bfc5cb 55%,#e3e6e8)" role="img" aria-label="Photo of a boardroom meeting"></div>
  <div class="abs" style="left:22px;top:22px;width:72px;height:86px;background:var(--navy);padding:12px 6px 0">
    <div style="color:#fff;font-weight:700;font-size:4.2px;margin-bottom:3px">LOREM IPSUM</div>
    <p class="lorem w">Lorem ipsum dolor sit amet, consectetur adipiscing elit, sed do eiusmod tempor incididunt ut labore et dolore magna aliqua. Ut enim ad minim veniam, quis nostrud exercitation ullamco laboris nisi ut aliquip ex ea commodo consequat. Duis aute irure dolor in reprehenderit.</p>
  </div>
  <div class="brand"><i></i>NORVANE</div>
</section>

<section class="slide" style="left:524px;top:869px">
  <div class="ttl">EDIT TITLE HERE</div>
  <div class="abs" style="left:0;top:20px;width:209px;height:88px;background:var(--grey-lt)"></div>
  <div class="abs" style="left:14px;top:26px;width:100px;display:flex;flex-direction:column;gap:5.6px">
    <div style="display:flex;align-items:center;gap:4px"><div class="box" style="position:static;width:6px;height:6px;font-size:3px">1</div><span class="cap" style="color:#555;font-weight:600">Lorem ipsum dolor sit amet, consectetur adipiscing elit</span></div>
    <div style="display:flex;align-items:center;gap:4px"><div class="box" style="position:static;width:6px;height:6px;font-size:3px">2</div><span class="cap" style="color:#555;font-weight:600">Lorem ipsum dolor sit amet, consectetur adipiscing elit</span></div>
    <div style="display:flex;align-items:center;gap:4px"><div class="box" style="position:static;width:6px;height:6px;font-size:3px">3</div><span class="cap" style="color:#555;font-weight:600">Lorem ipsum dolor sit amet, consectetur adipiscing elit</span></div>
    <div style="display:flex;align-items:center;gap:4px"><div class="box" style="position:static;width:6px;height:6px;font-size:3px">4</div><span class="cap" style="color:#555;font-weight:600">Lorem ipsum dolor sit amet, consectetur adipiscing elit</span></div>
    <div style="display:flex;align-items:center;gap:4px"><div class="box" style="position:static;width:6px;height:6px;font-size:3px">5</div><span class="cap" style="color:#555;font-weight:600">Lorem ipsum dolor sit amet, consectetur adipiscing elit</span></div>
    <div style="display:flex;align-items:center;gap:4px"><div class="box" style="position:static;width:6px;height:6px;font-size:3px">6</div><span class="cap" style="color:#555;font-weight:600">Lorem ipsum dolor sit amet, consectetur adipiscing elit</span></div>
  </div>
  <div class="photo" style="left:127px;top:20px;width:72px;height:88px;background:linear-gradient(170deg,#6f9bc6,#a9c3dc 35%,#4d6e8e 70%,#6f8f5a)" role="img" aria-label="Photo of a modern office building"></div>
  <div class="brand"><i></i>NORVANE</div>
</section>

<section class="slide" style="left:750px;top:869px">
  <div class="ttl">EDIT TITLE HERE</div>
  <div class="abs" style="left:13px;top:30px;width:183px;display:flex;gap:5px">
    <div style="flex:1"><div style="height:28px;background:linear-gradient(150deg,#3d5f85,#93a9be)" role="img" aria-label="Photo of a business setting"></div><div style="height:36px;background:var(--navy);padding:2px"><div style="color:#fff;font-size:2.2px;font-weight:700;text-align:center">TITLE HERE</div><p class="lorem w" style="font-size:1.8px;line-height:2.4px">Lorem ipsum dolor sit amet consectetur adipiscing elit sed do.</p></div></div>
    <div style="flex:1"><div style="height:28px;background:linear-gradient(150deg,#8c6a52,#c4a890)" role="img" aria-label="Photo of a business setting"></div><div style="height:36px;background:var(--grey);padding:2px"><div style="color:#fff;font-size:2.2px;font-weight:700;text-align:center">TITLE HERE</div><p class="lorem w" style="font-size:1.8px;line-height:2.4px">Lorem ipsum dolor sit amet consectetur adipiscing elit sed do.</p></div></div>
    <div style="flex:1"><div style="height:28px;background:linear-gradient(150deg,#b7c5d2,#6e8aa5)" role="img" aria-label="Photo of a business setting"></div><div style="height:36px;background:var(--navy);padding:2px"><div style="color:#fff;font-size:2.2px;font-weight:700;text-align:center">TITLE HERE</div><p class="lorem w" style="font-size:1.8px;line-height:2.4px">Lorem ipsum dolor sit amet consectetur adipiscing elit sed do.</p></div></div>
    <div style="flex:1"><div style="height:28px;background:linear-gradient(150deg,#5d7fa3,#d2c1b0)" role="img" aria-label="Photo of a business setting"></div><div style="height:36px;background:var(--grey);padding:2px"><div style="color:#fff;font-size:2.2px;font-weight:700;text-align:center">TITLE HERE</div><p class="lorem w" style="font-size:1.8px;line-height:2.4px">Lorem ipsum dolor sit amet consectetur adipiscing elit sed do.</p></div></div>
    <div style="flex:1"><div style="height:28px;background:linear-gradient(150deg,#7a8794,#c8ced4)" role="img" aria-label="Photo of a business setting"></div><div style="height:36px;background:var(--navy);padding:2px"><div style="color:#fff;font-size:2.2px;font-weight:700;text-align:center">TITLE HERE</div><p class="lorem w" style="font-size:1.8px;line-height:2.4px">Lorem ipsum dolor sit amet consectetur adipiscing elit sed do.</p></div></div>
    <div style="flex:1"><div style="height:28px;background:linear-gradient(150deg,#3f4f60,#8e9aa6)" role="img" aria-label="Photo of a business setting"></div><div style="height:36px;background:var(--grey);padding:2px"><div style="color:#fff;font-size:2.2px;font-weight:700;text-align:center">TITLE HERE</div><p class="lorem w" style="font-size:1.8px;line-height:2.4px">Lorem ipsum dolor sit amet consectetur adipiscing elit sed do.</p></div></div>
  </div>
  <div class="brand"><i></i>NORVANE</div>
</section>

<!-- Row 8 -->
<section class="slide no-rule" style="left:142px;top:1006px;background:#e4e4e4">
  <div class="abs" style="left:0;top:0;width:209px;height:58px;background:var(--navy)"></div>
  <div class="abs" style="left:10px;top:5px;color:#fff;font-weight:700;font-size:8px;line-height:8px">“</div>
  <p class="abs" style="left:22px;top:15px;width:166px;color:#fff;font-weight:700;font-size:3.3px;line-height:4.4px;text-align:center">“Lorem ipsum dolor sit amet, consectetur adipiscing elit. Phasellus sodales, ligula ultrices tempus tristique, tellus justo aliquam dui, nec lorem ipsum dolor sit amet, consectetur adipiscing elit. Lorem ipsum dolor sit amet, consectetur adipiscing.”</p>
  <div class="abs" style="right:10px;top:45px;color:#fff;font-weight:700;font-size:8px;line-height:8px">”</div>
  <div class="circ" style="left:88px;top:47px;width:33px;height:33px;background:#a5a5a5;border:1.5px solid #fff" role="img" aria-label="Portrait of the person quoted"></div>
  <div class="abs" style="left:0;top:84px;width:209px;text-align:center"><div style="font-size:3.6px;font-weight:600;color:#444">Laura Finn</div><div class="lorem">Chief Operating Officer</div></div>
</section>

<section class="slide" style="left:368px;top:1006px">
  <div class="ttl">EDIT TITLE HERE</div>
  <div class="photo" style="left:30px;top:20px;width:150px;height:80px;background:radial-gradient(ellipse at 50% 50%,#e4e4e4,#f3f3f3 70%)" role="img" aria-label="World map"></div>
  <svg class="abs" style="left:0;top:0" width="209" height="117"><g stroke="#9a9a9a" stroke-width=".4" fill="none"><path d="M50 30Q80 40 100 54 M100 54Q130 40 160 40 M100 54L100 80 M100 54Q130 70 150 80 M50 68Q80 60 100 54"/></g></svg>
  <div class="circ" style="left:46px;top:26px;width:8px;height:8px"></div>
  <div class="circ" style="left:58px;top:64px;width:8px;height:8px"></div>
  <div class="circ g" style="left:94px;top:48px;width:12px;height:12px"></div>
  <div class="circ" style="left:155px;top:36px;width:8px;height:8px"></div>
  <div class="circ" style="left:145px;top:76px;width:8px;height:8px"></div>
  <div class="abs" style="left:14px;top:26px;width:30px"><div class="cap">Lorem ipsum</div><p class="lorem">Lorem ipsum dolor sit amet, consectetur adipiscing elit. Phasellus sodales.</p></div>
  <div class="abs" style="left:14px;top:62px;width:40px"><div class="cap">Lorem ipsum</div><p class="lorem">Lorem ipsum dolor sit amet, consectetur adipiscing elit. Phasellus sodales.</p></div>
  <div class="abs" style="left:86px;top:64px;width:30px"><div class="cap">Lorem ipsum</div><p class="lorem">Lorem ipsum dolor sit amet, consectetur adipiscing elit. Phasellus sodales ligula.</p></div>
  <div class="abs" style="left:166px;top:34px;width:32px"><div class="cap">Lorem ipsum</div><p class="lorem">Lorem ipsum dolor sit amet, consectetur adipiscing elit. Phasellus sodales.</p></div>
  <div class="abs" style="left:155px;top:68px;width:40px"><div class="cap">Lorem ipsum</div><p class="lorem">Lorem ipsum dolor sit amet, consectetur adipiscing elit. Phasellus sodales.</p></div>
  <div class="brand"><i></i>NORVANE</div>
</section>

<section class="slide no-rule" style="left:595px;top:1006px">
  <div class="photo" style="left:0;top:0;width:209px;height:117px;background:linear-gradient(160deg,#1f4f80,#4f7ca8 45%,#9fb7cf 70%,#2d5a88)" role="img" aria-label="Photo looking up at glass office towers, tinted blue"></div>
  <div class="abs" style="left:0;top:31px;width:209px;text-align:center;color:#fff">
    <div style="font-size:11px;font-weight:400;letter-spacing:.4px;margin-bottom:6px">THANK YOU</div>
    <div style="font-size:3px;font-weight:700;line-height:4.2px">Norvane Vet Technologies ApS<br>Lindevej 12, 4000 Roskilde, Denmark<br>CVR no. 12345678</div>
    <div style="font-size:3px;font-weight:700;margin-top:4px">P: +45 20 00 00 00 &nbsp;•&nbsp; hello@norvanevet.dk</div>
  </div>
</section>

</body>
</html>
```